Genetics Lab Testing Flyers

I have 5 flyers for another laboratory that I will be working with that need to have the logos and colors changed to match our laboratory, all of the information is correct its just changing of the format, logo and color scheme. I have attached 2 versions of our logo as well. (silver birch labs)

Target Market(s)

physician offices

Industry/Entity Type

Healthcare - Laboratoy

Colors
0054AA
0677BA
7BADD7
CADEEF
E8F1F8

Requirements
Must have
• all the information on the 5 current flyers
Should not have
• any mention of TraxoKey

```html
<!DOCTYPE html>
<html lang="en">
<head>
<meta charset="utf-8">
<title>Government Initiative – Cancer Moonshot Flyer</title>
<link href="https://fonts.googleapis.com/css2?family=Roboto:wght@400;500;700&display=swap" rel="stylesheet">
<style>
:root{
  --blue-deep:#0054AA;
  --blue-mid:#0677BA;
  --blue-soft:#7BADD7;
  --blue-pale:#CADEEF;
  --blue-mist:#E8F1F8;
  --ink:#2b2b2b;
  --ink-grey:#555a60;
  --backdrop:#c4c4c4;
  --white:#ffffff;
}
*{box-sizing:border-box;margin:0;padding:0}
html,body{width:1015px;height:1200px;overflow:hidden}
body{background:var(--backdrop);font-family:"Roboto",Arial,sans-serif;color:var(--ink);position:relative}
.flyer{position:absolute;left:115px;top:92px;width:784px;height:1015px;background:var(--white);overflow:hidden}
.flyer-title{position:absolute;top:12px;left:0;width:100%;text-align:center;font-weight:700;font-size:31px;letter-spacing:.5px;color:var(--blue-deep)}
.headline-band{position:absolute;top:54px;left:0;width:100%;height:76px;background:linear-gradient(90deg,var(--blue-deep),var(--blue-mid));color:var(--white);text-align:center;font-weight:700;font-size:18px;line-height:24px;padding-top:14px}
.hero{position:absolute;top:130px;left:0;width:100%;height:325px;background:linear-gradient(90deg,#d7d9dc,#e4e6e8 45%,#eef0f2)}
.hero-photo{position:absolute;top:130px;left:330px;width:454px;height:430px;background:linear-gradient(135deg,#e9ecef 0%,#dfe3e8 40%,#cfd6de 70%,#b8c4d2 100%)}
.purpose{position:absolute;top:170px;left:42px;width:293px}
.purpose h2{font-size:18px;font-weight:700;color:var(--ink);margin-bottom:8px}
.purpose p{font-size:11.6px;line-height:18.5px;text-align:justify;color:var(--ink)}
.sweep{position:absolute;left:0;top:0;width:784px;height:1015px}
.content-panel{position:absolute;top:455px;left:0;width:763px;height:466px;background:var(--white)}
.section-heading{position:absolute;top:485px;left:0;width:784px;text-align:center;font-weight:700;font-size:18.5px;line-height:25px;color:var(--ink-grey)}
.col-heading{position:absolute;font-size:15px;font-weight:700;color:var(--ink)}
.item{position:absolute;width:340px;display:flex;align-items:flex-start}
.item-num{flex:0 0 23px;height:23px;border-radius:50%;background:linear-gradient(180deg,var(--blue-mid),var(--blue-deep));color:var(--white);font-size:11px;font-weight:700;display:flex;align-items:center;justify-content:center;margin-top:-1px}
.item-text{margin-left:11px;width:297px;font-size:11.7px;line-height:15.4px;text-align:justify}
.means-body{position:absolute;top:821px;left:401px;width:342px;font-size:11.7px;line-height:15.4px;text-align:justify}
.footer-rule{position:absolute;top:921px;left:0;width:100%;height:6px;background:var(--blue-soft)}
.footer{position:absolute;top:927px;left:0;width:100%;height:88px;background:linear-gradient(90deg,var(--blue-deep),var(--blue-mid) 60%,var(--blue-deep));color:var(--white);font-weight:700;font-size:12px;line-height:18.5px}
.brand{position:absolute;left:20px;top:22px;width:130px;text-align:center}
.brand-dot{width:24px;height:24px;border-radius:50%;border:2px solid var(--white);margin:0 auto 4px}
.brand-name{font-size:13px;font-weight:700;letter-spacing:.3px;line-height:15px}
.contact{position:absolute;top:20px;display:flex;align-items:flex-start}
.contact svg{flex:0 0 auto;margin-right:10px}
.divider{position:absolute;top:14px;width:1px;height:60px;background:rgba(255,255,255,.35)}
</style>
</head>
<body>
<div class="flyer">
  <h1 class="flyer-title">GOVERNMENT INITIATIVE</h1>
  <div class="headline-band">TO “END CANCER AS WE KNOW IT” (CANCER MOONSHOT)<br>RELEASES REPORT WITH STRONG SUPPORT FOR GENETIC TESTING</div>

  <div class="hero"></div>
  <div class="hero-photo" role="img" aria-label="Photo of two lab scientists in white coats and blue gloves, one pointing and one holding a tablet"></div>

  <section class="purpose">
    <h2>PURPOSE:</h2>
    <p>The “Cancer Moonshot” was announced by President Adam Harlow in his State of the Union address on January 12, 2016. Led by Vice President Lewis Crane, the ini tia tive is tasked with ending cancer as we know it, and doubling the rate of progress towards a cure. On September 7th, 2016 they released a statement with specifi recommendations.</p>
  </section>

  <div class="content-panel"></div>
  <svg class="sweep" viewBox="0 0 784 1015" aria-hidden="true">
    <polygon points="0,349 0,366 359,455 429,455" fill="#0054AA"/>
    <polygon points="0,392 207,443 0,495" fill="#0677BA"/>
    <polygon points="763,539 784,545 784,560 763,555" fill="#0054AA"/>
  </svg>

  <h2 class="section-heading">CANCER PREVENTION AND EARLY DETECTION IN INDIVIDUALS<br>AT HIGH RISK FOR CANCER</h2>

  <h3 class="col-heading" style="left:39px;top:546px">THE PLAN:</h3>
  <div class="item" style="left:43px;top:577px"><span class="item-num">1</span><p class="item-text">Develop effective strategies to scale up HBOC and LS screening and deliver evidencebased care</p></div>
  <div class="item" style="left:43px;top:623px"><span class="item-num">2</span><p class="item-text">Better insurance coverage for testing, particularly among poor and minority groups (with specific mention of Medicaid)</p></div>
  <div class="item" style="left:43px;top:684px"><span class="item-num">3</span><p class="item-text">Education of primary care providers to increase use of appropriate screening, counseling and evidencebased genetic tests</p></div>
  <div class="item" style="left:43px;top:746px"><span class="item-num">4</span><p class="item-text">Use of Next-Generation Sequencing to look at genes beyond just BRCA1, BRCA2 and the Lynch Syndrome genes</p></div>
  <div class="item" style="left:43px;top:807px"><span class="item-num">5</span><p class="item-text">Better general education so more people are aware of the genetics of cancer risk</p></div>
  <div class="item" style="left:43px;top:853px"><span class="item-num">6</span><p class="item-text">Testing of germline DNA for cancer patients along with testing their tumor</p></div>

  <h3 class="col-heading" style="left:398px;top:552px">THE PROBLEM:</h3>
  <div class="item" style="left:402px;top:583px"><span class="item-num">1</span><p class="item-text">“It is estimated that more than half of all cancer deaths could be prevented”</p></div>
  <div class="item" style="left:402px;top:629px"><span class="item-num">2</span><p class="item-text">“Underuse of germline (hereditary) cancer testing in appropriate populations is leading to unnecessarily lost lives and diminished quality of life”</p></div>
  <div class="item" style="left:402px;top:691px"><span class="item-num">3</span><p class="item-text">1-2 million people are living with BRCA and Lynch Syndrome mutations</p></div>
  <div class="item" style="left:402px;top:737px"><span class="item-num">4</span><p class="item-text">Less than 1.2% of people with Lynch Syndrome are aware of their status. Similarly, only a small percentage of BRCA mutation carriers know their status and risk</p></div>

  <h3 class="col-heading" style="left:401px;top:796px">WHAT THIS MEANS FOR YOU:</h3>
  <p class="means-body">The government is putting its weight behind cancer risk predisposition testing because of the proven benefits of such testing for your patients. As Medicare and other insurances shift from feeforservice to qualityand valuebased payments, a focus on prevention should also benefit the practice as well.</p>

  <div class="footer-rule"></div>
  <footer class="footer">
    <div class="brand">
      <div class="brand-dot"></div>
      <div class="brand-name">SILVER BIRCH LABS</div>
    </div>
    <div class="contact" style="left:183px">
      <svg width="18" height="26" viewBox="0 0 18 26" aria-hidden="true"><path d="M9 0C4 0 0 4 0 9c0 7 9 17 9 17s9-10 9-17c0-5-4-9-9-9zm0 13a4 4 0 1 1 0-8 4 4 0 0 1 0 8z" fill="#fff"/></svg>
      <div>48 Larchmont Rd.<br>Fairhaven, NJ 07704 U.S.A.</div>
    </div>
    <div class="divider" style="left:380px"></div>
    <div class="contact" style="left:399px">
      <svg width="30" height="20" viewBox="0 0 30 20" aria-hidden="true"><rect x="1" y="1" width="28" height="18" fill="none" stroke="#fff" stroke-width="2"/><path d="M1 1l14 11L29 1M1 19l10-9M29 19l-10-9" fill="none" stroke="#fff" stroke-width="2"/></svg>
      <div>Email :<br>info@silverbirchlabs.com</div>
    </div>
    <div class="divider" style="left:580px"></div>
    <div class="contact" style="left:598px">
      <svg width="28" height="30" viewBox="0 0 28 30" aria-hidden="true"><path d="M6 2l5 7-3 3c2 4 5 8 9 10l3-3 6 5-3 4C13 28 2 17 2 6z" fill="#fff"/><path d="M17 4a8 8 0 0 1 6 6M17 8a4 4 0 0 1 3 3" fill="none" stroke="#fff" stroke-width="1.6"/></svg>
      <div>Tel: (866) 555-0142<br>Tel: (201) 555-0186<br>Fax: (201) 555-0191</div>
    </div>
  </footer>
</div>
</body>
</html>
```